Project, Programme and Portfolio Management Consultant needs a business card

I have recently had someone create a brand guide for me and I wish to have new business cards that incorporate the new brand. I am an independent management consultant working with businesses to improve their ability to deliver their business strategy through selecting the right project, the right people and doing it in the right way. Whilst I am currently working on my own, I am hoping to start to build win business where I need to bring in a team and this branding activity is the start of that process.

Target Market(s)

Medium to large businesses, government departments and defence

Contact Information for Business Card

Name
job title
business name
mobile
email
website
linkedIn profile

Font styles to use
Other font styles liked:
• roboto light

Colors

Designer to choose colors to be used in the design.

Requirements
Must have
• Must use my logo and brand colours (see attached brand guide)

```html
<!DOCTYPE html>
<html lang="en">
<head>
<meta charset="utf-8">
<title>Northvale Consulting – Business Card</title>
<link rel="stylesheet" href="https://fonts.googleapis.com/css2?family=Lato:wght@400;700&display=swap">
<style>
  :root {
    --page-bg: #d8d2ca;
    --card-face: #eeebe6;
    --navy: #163a5c;
    --navy-deep: #0f2c48;
    --gold: #d99a1e;
    --teal: #1a9c84;
    --text-gold: #d9a232;
  }
  html, body {
    margin: 0;
    width: 1200px;
    height: 1047px;
    overflow: hidden;
    background: var(--page-bg);
    font-family: "Lato", Arial, sans-serif;
  }
  .card {
    position: absolute;
    left: 120px;
    top: 263px;
    width: 960px;
    height: 520px;
    border-radius: 22px;
    overflow: hidden;
    background: var(--card-face);
    box-shadow: 0 10px 30px rgba(0,0,0,0.15);
  }
  .card-shapes {
    position: absolute;
    inset: 0;
  }
  .identity {
    position: absolute;
    left: 50px;
    top: 80px;
  }
  .name {
    margin: 0;
    font-size: 40px;
    font-weight: 700;
    color: var(--teal);
    line-height: 1.1;
  }
  .title {
    margin: 4px 0 0;
    font-size: 20px;
    color: var(--text-gold);
  }
  .company {
    position: absolute;
    left: 50px;
    top: 248px;
    color: var(--text-gold);
    font-size: 21px;
    line-height: 27px;
  }
  .company-name {
    display: block;
    font-weight: 700;
    color: var(--teal);
    font-size: 20px;
    letter-spacing: 0.3px;
  }
  .contacts {
    position: absolute;
    left: 50px;
    top: 342px;
    margin: 0;
    padding: 0;
    list-style: none;
  }
  .contacts li {
    display: flex;
    align-items: center;
    height: 30px;
    font-size: 21px;
    color: var(--text-gold);
  }
  .contacts svg {
    width: 20px;
    height: 20px;
    margin-right: 20px;
    flex: none;
  }
  .wordmark {
    position: absolute;
    left: 600px;
    top: 230px;
    width: 300px;
    display: flex;
    align-items: center;
    justify-content: center;
    gap: 14px;
  }
  .wordmark-dot {
    width: 26px;
    height: 26px;
    border-radius: 50%;
    background: var(--gold);
  }
  .wordmark-name {
    font-size: 44px;
    font-weight: 700;
    color: var(--navy);
  }
</style>
</head>
<body>
  <div class="card">
    <svg class="card-shapes" viewBox="0 0 960 520" width="960" height="520" aria-hidden="true">
      <defs>
        <linearGradient id="panelShade" x1="0" y1="0" x2="1" y2="1">
          <stop offset="0" stop-color="#1d4468"/>
          <stop offset="1" stop-color="#0f2c48"/>
        </linearGradient>
      </defs>
      <path d="M566 0 Q452 250 542 520" fill="none" stroke="var(--gold)" stroke-width="10"/>
      <path d="M0 0 H554 Q440 250 528 520 H0 Z" fill="url(#panelShade)"/>
    </svg>

    <div class="identity">
      <h1 class="name">Clara Wendell</h1>
      <p class="title">Founder &amp; CEO</p>
    </div>

    <div class="company">
      <span class="company-name">NORTHVALE CONSULTING LLC</span>
      48 Harbor Lane,<br>
      3rd FL Easton, CT 06612
    </div>

    <ul class="contacts">
      <li>
        <svg viewBox="0 0 20 20"><path d="M5 2 L8 6 L6.5 8 Q8 12 12 13.5 L14 12 L18 15 L16 18 Q6 17 2 5 Z" fill="var(--teal)"/></svg>
        555 014 2290
      </li>
      <li>
        <svg viewBox="0 0 20 20"><rect x="2" y="4" width="16" height="12" fill="var(--teal)"/><path d="M2 4 L10 11 L18 4" fill="none" stroke="var(--navy)" stroke-width="1.5"/></svg>
        hello@northvale.co
      </li>
      <li>
        <svg viewBox="0 0 20 20" fill="none" stroke="var(--teal)" stroke-width="1.5"><circle cx="10" cy="10" r="8"/><ellipse cx="10" cy="10" rx="3.5" ry="8"/><path d="M2 10 H18"/></svg>
        www.northvale.co
      </li>
      <li>
        <svg viewBox="0 0 20 20"><circle cx="10" cy="10" r="8" fill="none" stroke="var(--teal)" stroke-width="1.5"/></svg>
        profile.northvale.co/clara
      </li>
    </ul>

    <div class="wordmark">
      <span class="wordmark-dot"></span>
      <span class="wordmark-name">Northvale</span>
    </div>
  </div>
</body>
</html>
```